Pharmacy

Two sided postcard. Pictures on one side. Description on the other. We design and build pharmacies. pictures are some of our finished work. You can use as many pictures as you like not necessary to use all of them. Size of card should be 5"x7". See my website at display@brightmorefixtures.com for more inspiration. I include the back of one card that I used recently. Both sids need design input. Feel free to contact me with questions.
Requirements
Must have
- Must be a two sided postcard
Nice to have
- I am sending a design of a sleek type postcard that I saw online as an example.
- https://pixlink.example/images/k7WqRt
- I am looking for something modern.
- Not limited to colors on my website.

```html
<!DOCTYPE html>
<html lang="en">
<head>
<meta charset="utf-8">
<title>Brightmore Fixture &amp; Display – Postcard</title>
<link rel="stylesheet" href="https://fonts.googleapis.com/css2?family=Open+Sans:wght@400;600;700&family=Tinos:ital,wght@0,400;0,700;1,400&family=Arimo:wght@400;700&display=swap">
<style>
  :root {
    --maroon: #731316;
    --cream: #e6cfa8;
    --cream-light: #f0e0c4;
    --navy: #1d2440;
    --white: #ffffff;
    --ink: #333333;
    --stage: #e9e7e4;
  }
  * { box-sizing: border-box; margin: 0; padding: 0; }
  html, body { width: 874px; height: 1200px; overflow: hidden; }
  body {
    position: relative;
    background: var(--stage);
    font-family: "Open Sans", Arial, sans-serif;
  }
  .card {
    position: absolute;
    left: 88px;
    width: 699px;
    height: 500px;
    overflow: hidden;
    box-shadow: 0 3px 8px rgba(0,0,0,.25);
  }
  .card--front { top: 76px; }
  .card--back  { top: 635px; background: var(--white); }

  /* Front */
  .front__photo {
    position: absolute; inset: 0;
    background: linear-gradient(160deg, #d9cbbd 0%, #9a7660 35%, #5a3a2a 60%, #d8d6d2 100%);
  }
  .front__shapes { position: absolute; inset: 0; }
  .front__headline {
    position: absolute; left: 24px; top: 82px;
    color: var(--white); font-weight: 700; font-size: 30px; line-height: 40px;
    text-transform: uppercase;
  }
  .front__company {
    position: absolute; left: 24px; top: 414px;
    color: var(--white); font-weight: 600; font-size: 15px;
  }
  .front__contact {
    position: absolute; left: 24px; top: 444px;
    color: var(--white); font-size: 15px; line-height: 21px;
  }
  .contact-line { display: flex; align-items: center; gap: 6px; }
  .icon-dot {
    width: 16px; height: 16px; border-radius: 50%; background: var(--white);
    display: inline-flex; align-items: center; justify-content: center;
  }
  .badge {
    position: absolute; left: 508px; top: 326px; width: 164px; height: 164px;
  }
  .badge svg { position: absolute; inset: 0; }
  .badge__text {
    position: absolute; inset: 0; display: flex; flex-direction: column;
    align-items: center; justify-content: center;
    font-family: "Tinos", "Times New Roman", serif; color: var(--navy);
    font-weight: 700; font-size: 11.5px; line-height: 19px; text-transform: uppercase; text-align: center;
  }
  .badge__since { font-weight: 400; font-style: italic; }

  /* Back */
  .back__shapes { position: absolute; inset: 0; }
  .back__company {
    position: absolute; left: 13px; top: 39px;
    color: var(--white); font-weight: 600; font-size: 17px;
  }
  .back__tagline {
    position: absolute; left: 0; top: 75px; width: 412px; height: 36px;
    background: var(--cream);
    font-family: "Tinos", "Times New Roman", serif; font-weight: 700; font-size: 16.5px;
    color: var(--navy); line-height: 36px; padding-left: 18px; letter-spacing: .3px;
  }
  .gallery { position: absolute; left: 18px; top: 131px; display: flex; gap: 6px; }
  .gallery__item { width: 108px; height: 89px; border: 2px solid var(--cream-light); }
  .gallery__item--a { background: linear-gradient(135deg, #7a4a30, #c7b8a6 60%, #6b4a36); }
  .gallery__item--b { background: linear-gradient(135deg, #e0dcd6, #8c8f99 50%, #5d6e8a); }
  .gallery__item--c { background: linear-gradient(135deg, #c9cdd2, #8a9cb4 50%, #7b4a2e); }
  .back__copy {
    position: absolute; left: 17px; top: 240px; width: 323px;
    color: var(--white); font-size: 12.3px; line-height: 15.5px; text-align: justify;
  }
  .back__copy p + p { margin-top: 15px; }
  .back__cta {
    position: absolute; left: 0; top: 400px; width: 357px; height: 37px;
    background: var(--cream); color: var(--maroon);
    display: flex; align-items: center; justify-content: center; gap: 8px;
    font-weight: 600; font-size: 16.5px;
  }
  .back__email {
    position: absolute; left: 0; top: 449px; width: 357px; text-align: center;
    color: var(--white); font-size: 13.5px; line-height: 18px;
  }
  .mail-address {
    position: absolute; left: 455px; top: 45px; font-style: normal;
    font-family: "Arimo", Arial, sans-serif; font-size: 12px; line-height: 15px; color: var(--ink);
  }
  .postage {
    position: absolute; left: 595px; top: 34px; width: 73px; height: 73px;
    border: 1px solid #555; font-family: "Arimo", Arial, sans-serif;
    font-size: 9.5px; line-height: 11.5px; color: #111; text-align: center;
    display: flex; flex-direction: column; justify-content: center;
  }
  .postage b { font-weight: 700; }
</style>
</head>
<body>

<section class="card card--front">
  <div class="front__photo" role="img" aria-label="Photo of a finished pharmacy interior with glass cosmetics counters and wood shelving"></div>
  <svg class="front__shapes" width="699" height="500" viewBox="0 0 699 500">
    <path d="M0 340 C 200 395, 470 400, 699 300 L699 500 L0 500 Z" fill="var(--cream)"/>
    <path d="M0 350 C 200 405, 470 410, 699 312 L699 500 L0 500 Z" fill="var(--maroon)"/>
  </svg>
  <h1 class="front__headline">A complete service<br>from design thru<br>installation</h1>
  <p class="front__company">Brightmore Fixture &amp; Display Co. Inc</p>
  <div class="front__contact">
    <div class="contact-line">
      <span class="icon-dot"><svg width="10" height="10" viewBox="0 0 24 24"><path fill="var(--maroon)" d="M6.6 10.8a15 15 0 0 0 6.6 6.6l2.2-2.2c.3-.3.7-.4 1-.2 1.1.4 2.3.6 3.6.6.6 0 1 .4 1 1V20c0 .6-.4 1-1 1A17 17 0 0 1 3 4c0-.6.4-1 1-1h3.5c.6 0 1 .4 1 1 0 1.3.2 2.5.6 3.6.1.3 0 .7-.2 1z"/></svg></span>
      201 555 0148
    </div>
    <div class="contact-line">
      <span class="icon-dot"><svg width="11" height="11" viewBox="0 0 24 24" fill="none" stroke="var(--maroon)" stroke-width="2"><circle cx="12" cy="12" r="9"/><path d="M3 12h18M12 3c3 3 3 15 0 18M12 3c-3 3-3 15 0 18"/></svg></span>
      www.display@brightmorefixtures.com
    </div>
  </div>
  <div class="badge">
    <svg width="164" height="164" viewBox="0 0 164 164">
      <polygon fill="var(--cream)" points="82,4 89,17 98,6 102,20 113,10 114,25 126,18 124,33 138,28 133,42 147,40 140,53 154,54 144,65 158,69 146,78 159,85 146,91 157,100 143,104 152,115 138,116 144,129 130,127 133,141 119,136 119,151 107,143 104,157 94,147 88,160 82,148 76,160 70,147 60,157 57,143 45,151 45,136 31,141 34,127 20,129 26,116 12,115 21,104 7,100 18,91 5,85 18,78 6,69 20,65 10,54 24,53 17,40 31,42 26,28 40,33 38,18 50,25 51,10 62,20 66,6 75,17"/>
      <circle cx="82" cy="82" r="68" fill="var(--cream)"/>
    </svg>
    <div class="badge__text">
      <span>Tree generation</span>
      <span>specializing</span>
      <span>in pharmacy design</span>
      <span class="badge__since">Since 1917</span>
    </div>
  </div>
</section>

<section class="card card--back">
  <svg class="back__shapes" width="699" height="500" viewBox="0 0 699 500">
    <path d="M458 0 Q 362 220 357 500" fill="none" stroke="var(--cream)" stroke-width="10"/>
    <path d="M0 0 L445 0 Q 350 220 345 500 L0 500 Z" fill="var(--maroon)"/>
  </svg>
  <h2 class="back__company">Brightmore Fixture &amp; Display Co. Inc</h2>
  <div class="back__tagline">QUALITY - EXPERIENCE - INNOVATION</div>
  <div class="gallery">
    <div class="gallery__item gallery__item--a" role="img" aria-label="Pharmacy aisle with wood shelving"></div>
    <div class="gallery__item gallery__item--b" role="img" aria-label="Pharmacy interior with gondola displays"></div>
    <div class="gallery__item gallery__item--c" role="img" aria-label="Pharmacy end-cap display unit"></div>
  </div>
  <div class="back__copy">
    <p>Family owned and operated for three generations.</p>
    <p>Brightmore Fixture &amp; Display Co. Inc is the oldest store fixture company in New Jersey. As designers &amp; Manufacturers we can save you hours of time and money.</p>
    <p>Our level of experience will be evident from the outset and you will be pleased that you found us.</p>
  </div>
  <div class="back__cta">
    <span>CONTACT US</span>
    <svg width="18" height="18" viewBox="0 0 24 24"><circle cx="12" cy="12" r="10.5" fill="none" stroke="var(--maroon)" stroke-width="2"/><path transform="translate(5.5 5.5) scale(.55)" fill="var(--maroon)" d="M6.6 10.8a15 15 0 0 0 6.6 6.6l2.2-2.2c.3-.3.7-.4 1-.2 1.1.4 2.3.6 3.6.6.6 0 1 .4 1 1V20c0 .6-.4 1-1 1A17 17 0 0 1 3 4c0-.6.4-1 1-1h3.5c.6 0 1 .4 1 1 0 1.3.2 2.5.6 3.6.1.3 0 .7-.2 1z"/></svg>
    <span>201 555 0148</span>
  </div>
  <div class="back__email">
    display@brightmorefixtures.com<br>
    www.display@brightmorefixtures.com
  </div>
  <address class="mail-address">
    Brightmore Fixture &amp;<br>
    Display Co. Inc<br>
    PO Box 318<br>
    Ridgefield NJ 07657
  </address>
  <div class="postage">
    <span>presorted</span>
    <span>FIRST CLASS</span>
    <span>U.S. Postage</span>
    <b>PAID</b>
    <span>Postrun</span>
  </div>
</section>

</body>
</html>
```